R. T. HOLLOWAY, INC. is a US based Investment firm looking for a five-page website design.

Currently, their temporary site is located at: rtholloway.example and they would like to maintain the site design as much as possible.

R. T. HOLLOWAY, INC. sister companies are: Crestway Lodge Investments (c-lodge.example) Benwick Petroleum (benwick-petroleum.example) and RTHF (rth-foundation.example/en)

Attached is a .ZIP file with designs and assets we think will be useful for your proposal… Content for the site is attached on: rtholloway website content.docx Current temp website design is attached as: Coming Soon Website.zip .EPS Logo files attached as: rtholloway logos.zip Sample business card attached as: R T Holloway Business cards.eps Other assets, such as Fonts and background images attached as: Assets.zip

Target Market(s)

Investors

Industry/Entity Type

Investments

Number of Pages Required

5+ page

Requirements
Must have
• Contact Page with a form.

```html
<!DOCTYPE html>
<html lang="en">
<head>
<meta charset="utf-8">
<title>R. T. Holloway, Inc.</title>
<link href="https://fonts.googleapis.com/css2?family=Cinzel:wght@400;500&family=Montserrat:wght@400;500;600&family=Arimo:wght@400&display=swap" rel="stylesheet">
<style>
:root{
  --gold:#a88c4a;
  --gold-light:#b99c56;
  --navy:#17202e;
  --navy-deep:#0f1a28;
  --ink:#333333;
  --grey:#555555;
  --white:#ffffff;
}
*{margin:0;padding:0;box-sizing:border-box}
html,body{width:1200px;height:3859px;overflow:hidden;background:var(--white)}
body{position:relative;font-family:"Arimo",Arial,sans-serif;color:var(--ink)}
.abs{position:absolute}
.topline{left:0;top:0;width:1200px;height:5px;background:var(--navy)}
.topline::after{content:"";position:absolute;left:772px;top:0;width:428px;height:5px;background:var(--gold)}
.wordmark{font-family:"Montserrat",sans-serif;font-weight:600;white-space:nowrap;letter-spacing:.5px}
.brand{left:112px;top:74px;font-size:20px;color:var(--navy)}
.nav a{position:absolute;top:80px;font-family:"Montserrat",sans-serif;font-size:14px;font-weight:500;color:var(--ink);text-decoration:none;white-space:nowrap}
.nav a.active{color:var(--gold)}
.hero-photo{left:0;top:160px;width:1200px;height:800px}
.hero-title{left:112px;top:400px;font-family:"Cinzel",serif;font-size:56px;font-weight:400;color:var(--gold);white-space:nowrap}
.hero-sub{left:112px;top:482px;font-family:"Montserrat",sans-serif;font-size:17px;line-height:31px;color:var(--white);font-weight:500}
.btn{position:absolute;display:flex;align-items:center;justify-content:center;background:var(--gold);color:var(--white);font-family:"Montserrat",sans-serif;font-size:16px;font-weight:500;text-decoration:none;border-radius:2px}
.btn.serif{font-family:"Cinzel",serif;font-size:17px}
.section-title{font-family:"Montserrat",sans-serif;font-weight:500;letter-spacing:1px}
.services-title{left:0;width:1200px;top:1012px;text-align:center;font-size:34px;color:var(--ink)}
.rule{position:absolute;height:4px;width:46px;background:var(--gold)}
.svc{position:absolute;width:260px}
.svc h3{font-family:"Montserrat",sans-serif;font-weight:500;font-size:18px;color:var(--ink);margin-bottom:6px}
.svc p{font-size:14px;color:var(--grey)}
.svc.right{text-align:right}
.center-mark{left:454px;top:1350px;width:278px;text-align:center;font-size:19px;color:var(--white)}
.about-title{left:112px;top:1832px;font-size:42px;color:var(--white)}
.about-text{left:112px;top:1910px;width:465px;font-size:13.5px;line-height:25.7px;color:var(--white);text-align:justify}
.lead-title{left:714px;top:2486px;font-size:36px;color:var(--ink)}
.lead-text{left:715px;top:2568px;width:370px;font-size:13.2px;line-height:25.8px;color:var(--grey);text-align:justify}
.lead-frame{left:133px;top:2467px;width:541px;height:417px;border:2px solid var(--gold)}
.quote-text{left:568px;top:3072px;width:484px;font-size:13.2px;line-height:29.2px;color:var(--white);text-align:justify}
.quote-name{left:568px;top:3293px;font-family:"Montserrat",sans-serif;font-size:18px;font-weight:500;color:var(--white)}
.stars{left:568px;top:3323px;color:var(--white);font-size:15px;letter-spacing:2px}
.foot-brand{left:0;width:1200px;top:3600px;text-align:center;font-size:30px;color:var(--white)}
.foot-nav a{position:absolute;top:3688px;font-family:"Montserrat",sans-serif;font-size:14px;font-weight:500;color:var(--white);text-decoration:none;white-space:nowrap}
.social{position:absolute;top:3737px;width:40px;height:40px;border:2px solid var(--white);border-radius:50%}
.copyright{left:0;width:1200px;top:3801px;text-align:center;font-size:14px;color:var(--white)}
</style>
</head>
<body>

<div class="abs topline"></div>

<header>
  <div class="abs wordmark brand">R. T. HOLLOWAY, INC.</div>
  <nav class="nav">
    <a class="active" href="#" style="left:421px">HOME</a>
    <a href="#" style="left:497px">ABOUT US</a>
    <a href="#" style="left:605px">INVESTMENT AREAS</a>
    <a href="#" style="left:784px">SOCIAL RESPONSIBILITY</a>
    <a href="#" style="left:994px">CONTACT US</a>
  </nav>
</header>

<section class="hero">
  <svg class="abs hero-photo" width="1200" height="800" viewBox="0 0 1200 800" role="img" aria-label="Hand holding a glowing rising financial bar chart on a dark blue background">
    <defs>
      <radialGradient id="heroGlow" cx="0.68" cy="0.45" r="0.55">
        <stop offset="0" stop-color="#5c4a52"/>
        <stop offset="0.45" stop-color="#24344a"/>
        <stop offset="1" stop-color="#0f1a28"/>
      </radialGradient>
    </defs>
    <path d="M0 0H1200V632Q600 957 0 632Z" fill="var(--gold)"/>
    <path d="M0 0H1200V620Q600 920 0 620Z" fill="url(#heroGlow)"/>
  </svg>
  <h1 class="abs hero-title">RT Holloway</h1>
  <p class="abs hero-sub">SED UT PERSPICIATIS UNDE OMNIS ISTE NATUS<br>ERROR SIT VOLUPTATEM ACCUSANTIUM</p>
  <a class="btn serif" href="#" style="left:112px;top:562px;width:140px;height:51px">READ MORE</a>
</section>

<section class="services">
  <h2 class="abs section-title services-title">OUR SERVICES</h2>
  <div class="rule" style="left:577px;top:1065px"></div>

  <svg class="abs" style="left:0;top:1100px" width="1200" height="560" viewBox="0 1100 1200 560">
    <circle cx="593" cy="1362" r="177" fill="none" stroke="var(--navy)" stroke-width="4"/>
    <circle cx="593" cy="1362" r="139" fill="var(--gold)"/>
    <circle cx="476" cy="1229" r="10" fill="var(--gold)"/>
    <circle cx="709" cy="1229" r="10" fill="var(--gold)"/>
    <circle cx="475" cy="1496" r="10" fill="var(--gold)"/>
    <circle cx="707" cy="1496" r="10" fill="var(--gold)"/>
    <circle cx="416" cy="1354" r="11" fill="var(--navy)"/>
    <circle cx="768" cy="1354" r="11" fill="var(--navy)"/>

    <g fill="none" stroke="var(--white)" stroke-width="2.2" stroke-linecap="round" stroke-linejoin="round">
      <circle cx="360" cy="1177" r="54" fill="var(--gold)" stroke="none"/>
      <path d="M344 1152h24l10 10v40h-34z M368 1152v10h10 M352 1170h18 M352 1180h18 M352 1190h12"/>
      <circle cx="827" cy="1177" r="54" fill="var(--gold)" stroke="none"/>
      <path d="M804 1158h38v38h-38z M812 1150h38v38 M804 1186l28-28 M804 1176l18-18 M814 1196l28-28"/>
      <circle cx="300" cy="1357" r="54" fill="var(--navy)" stroke="none"/>
      <path d="M284 1348l8 8 8-12 8 12 8-8-4 16h-24z M276 1372l14 12h20l14-12"/>
      <circle cx="870" cy="1357" r="54" fill="var(--navy)" stroke="none"/>
      <circle cx="870" cy="1350" r="16"/><path d="M862 1370h16 M864 1377h12 M870 1326v-6 M848 1350h-6 M892 1350h6"/>
      <circle cx="360" cy="1555" r="54" fill="var(--gold)" stroke="none"/>
      <circle cx="350" cy="1534" r="6"/><path d="M340 1578v-32h20v32 M366 1542h14 M366 1556h14 M366 1570h14"/>
      <circle cx="828" cy="1555" r="54" fill="var(--gold)" stroke="none"/>
      <circle cx="828" cy="1532" r="6"/><path d="M818 1548h20 M828 1548v10 M808 1560h40 M808 1560v6 M828 1560v6 M848 1560v6"/>
      <circle cx="808" cy="1572" r="5"/><circle cx="828" cy="1572" r="5"/><circle cx="848" cy="1572" r="5"/>
    </g>
  </svg>

  <div class="abs wordmark center-mark">R. T. HOLLOWAY, INC.</div>

  <div class="svc right" style="left:22px;top:1154px"><h3>Integrity</h3><p>Sed ut perspiciatis unde omnis</p></div>
  <div class="svc" style="left:899px;top:1151px"><h3>Transparency</h3><p>Sed ut perspiciatis unde omnis</p></div>
  <div class="svc right" style="left:-28px;top:1335px"><h3>Excellence</h3><p>Sed ut perspiciatis unde omnis</p></div>
  <div class="svc" style="left:941px;top:1329px"><h3>Innovation</h3><p>Sed ut perspiciatis unde omnis</p></div>
  <div class="svc right" style="left:22px;top:1541px"><h3>Responsibility</h3><p>Sed ut perspiciatis unde omnis</p></div>
  <div class="svc" style="left:906px;top:1534px"><h3>Organization</h3><p>Sed ut perspiciatis unde omnis</p></div>
</section>

<section class="about">
  <svg class="abs" style="left:0;top:1678px" width="1200" height="700" viewBox="0 1678 1200 700" role="img" aria-label="Hand holding a glowing light bulb beside stacks of coins">
    <defs>
      <linearGradient id="aboutTone" x1="0" y1="0" x2="1" y2="1">
        <stop offset="0" stop-color="#1f2530"/>
        <stop offset="0.45" stop-color="#3a3226"/>
        <stop offset="0.8" stop-color="#8a6a3a"/>
        <stop offset="1" stop-color="#c79a55"/>
      </linearGradient>
    </defs>
    <path d="M0 1798Q600 1560 1200 1798V2247Q600 2500 0 2247Z" fill="url(#aboutTone)"/>
  </svg>
  <h2 class="abs section-title about-title">ABOUT US</h2>
  <div class="rule" style="left:112px;top:1893px;width:64px;height:3px"></div>
  <p class="abs about-text">Based in Houston, Texas, R. T. Holloway, Inc. is an investment company, founded in 2010, with the purpose to foster endeavors for socioeconomic development, and create platforms for harnessing the potential of world resources, designed to meet the demands of the emerging markets. R. T. Holloway, Inc. functions as a vehicle that enables investments, with the goal of developing the multiple opportunities available.</p>
  <a class="btn" href="#" style="left:112px;top:2093px;width:141px;height:54px">READ MORE</a>
</section>

<section class="leadership">
  <div class="abs" role="img" aria-label="Businessman pointing at financial charts on a desk" style="left:117px;top:2479px;width:545px;height:420px;background:linear-gradient(120deg,#f2c58a 0%,#b9b7b8 40%,#6f8fb8 75%,#2f4f7d 100%)"></div>
  <div class="abs lead-frame"></div>
  <h2 class="abs section-title lead-title">LEADERSHIP</h2>
  <div class="rule" style="left:715px;top:2543px;width:64px;height:4px"></div>
  <p class="abs lead-text">R. T. Holloway, Inc. is headed by Ronald P. Thayer Holloway, Lorem ipsum dolor sit amet, consectetur adipiscing elit. Cura bitur non quam ultricies, facilisis quam a, efficitur dolor. Morbi eget neque placerat eros aliquam commodo. Phasellus lobortis diam pretium, blandit nulla ac, congue lacus. Mauris faucibus accumsan lacus, id aliquam nunc rutrum ut. Mauris nec tortor a ante porttitor bibendum sed sit amet elit. Phas ellus condimentum ac tortor vitae tincidunt. Vivamus element dolor sedum nec nulla et posuere.</p>
  <a class="btn" href="#" style="left:715px;top:2823px;width:135px;height:51px">READ MORE</a>
</section>

<section class="testimonial">
  <svg class="abs" style="left:0;top:2975px" width="1200" height="884" viewBox="0 2975 1200 884">
    <rect x="0" y="2975" width="1200" height="884" fill="var(--navy)"/>
    <path d="M0 2975H1200V3385Q600 3580 0 3385Z" fill="var(--gold)"/>
    <circle cx="336" cy="3212" r="177" fill="#c9c2b8" role="img" aria-label="Smiling man with a tablet, seated"/>
  </svg>
  <p class="abs quote-text">Sed ut perspiciatis unde omnis iste natus error sit voluptatem accusantium doloremque laudantium, totam rem aperiam, eaque ipsa quae ab illo inventore veritatis et quasi architecto beatae vitae dicta sunt explicabo. Nemo enim ipsam voluptatem quia voluptas sit aspernatur aut odit aut fugit, sed quia consequuntur magni dolores eos qui ratione voluptatem sequi nesciunt. Neque porro quisquam est, qui dolorem ipsum quia dolor sit amet, consectetur, adipisci velit, sed quia ut labore et dolore magnam aliquam quaerat voluptatem.</p>
  <div class="abs quote-name">MARCUS ELLERY</div>
  <div class="abs stars">★★★★★</div>
</section>

<footer>
  <div class="abs wordmark foot-brand">R. T. HOLLOWAY, INC.</div>
  <nav class="foot-nav">
    <a href="#" style="left:245px">HOME</a>
    <a href="#" style="left:325px">ABOUT US</a>
    <a href="#" style="left:440px">INVESTMENT AREAS</a>
    <a href="#" style="left:631px">SOCIAL RESPONSIBILITY</a>
    <a href="#" style="left:854px">CONTACT US</a>
  </nav>
  <span class="social" style="left:484px"></span>
  <span class="social" style="left:532px"></span>
  <span class="social" style="left:580px"></span>
  <span class="social" style="left:628px"></span>
  <span class="social" style="left:674px"></span>
  <p class="abs copyright">© Copyrights 2021 RT Holloway.All Rights Reserved.</p>
</footer>

</body>
</html>
```